Local electrical company needs two flyers designed

We are a small local electrical contracting company and are in desperate need of a awasome flyer design to help grow our business
Updates

hi everyone.

please keep the logo off the front page.
it can go on the rear.

We are really trying to portray a angry/frustrated women BECAUSE her lights are broken.
not light globes

Target Market(s)

Home owners

Industry/Entity Type

Electrical

Font styles to use
Serif

```html
<!DOCTYPE html>
<html lang="en">
<head>
<meta charset="utf-8">
<title>Lighting replacement flyer</title>
<link rel="stylesheet" href="https://fonts.googleapis.com/css2?family=Gelasio:wght@400;700&family=Open+Sans:wght@600&display=swap">
<style>
  :root {
    --page-white: #ffffff;
    --frame-black: #1a1a1a;
    --green-deep: #004526;
    --green-mid: #4a8a2a;
    --green-lime: #b8cf00;
    --tag-green: #00a04a;
    --ink-dark: #1c1c1c;
    --text-white: #ffffff;
    --silver-light: #e6e8ea;
    --silver-mid: #b9bdc1;
  }
  html, body {
    margin: 0;
    padding: 0;
    overflow: hidden;
    background: var(--page-white);
  }
  .canvas {
    position: relative;
    width: 1200px;
    height: 840px;
    box-sizing: border-box;
    border: 1px solid var(--frame-black);
    background: var(--page-white);
    overflow: hidden;
  }
  .flyer {
    position: absolute;
    left: 58px;
    top: 58px;
    width: 1084px;
    height: 724px;
    box-sizing: border-box;
    border: 1px solid var(--frame-black);
    background: linear-gradient(180deg, var(--green-deep) 0%, var(--green-deep) 8%, var(--green-mid) 45%, var(--green-lime) 85%, var(--green-lime) 100%);
    overflow: hidden;
  }
  .category-tag {
    position: absolute;
    right: 0;
    top: 0;
    width: 399px;
    height: 78px;
    background: var(--tag-green);
    color: var(--ink-dark);
    font-family: "Open Sans", Arial, sans-serif;
    font-weight: 600;
    font-size: 25px;
    line-height: 78px;
    text-align: center;
    margin: 0;
  }
  .product-photo {
    position: absolute;
    left: 530px;
    top: 235px;
    width: 545px;
    height: 345px;
  }
  .headline,
  .subline,
  .wallet-line {
    position: absolute;
    left: 60px;
    margin: 0;
    font-family: "Gelasio", Georgia, serif;
  }
  .headline {
    top: 88px;
    color: var(--text-white);
    font-weight: 700;
    font-size: 78px;
    line-height: 76px;
    letter-spacing: -0.5px;
  }
  .subline {
    top: 300px;
    color: var(--text-white);
    font-weight: 400;
    font-size: 44px;
    line-height: 56px;
  }
  .wallet-line {
    top: 395px;
    color: var(--ink-dark);
    font-weight: 700;
    font-size: 98px;
    line-height: 82px;
    letter-spacing: -0.5px;
  }
</style>
</head>
<body>
<div class="canvas">
  <section class="flyer">
    <p class="category-tag">Lighting replacement</p>

    <svg class="product-photo" viewBox="0 0 545 345" role="img" aria-label="Photo of a silver LED recessed downlight with five lenses beside its white power driver">
      <defs>
        <radialGradient id="downlight-tone" cx="0.6" cy="0.4" r="0.65">
          <stop offset="0" stop-color="var(--silver-light)"/>
          <stop offset="1" stop-color="var(--silver-mid)"/>
        </radialGradient>
      </defs>
      <ellipse cx="330" cy="160" rx="210" ry="160" fill="url(#downlight-tone)"/>
    </svg>

    <h1 class="headline">Tired of<br>replacing bulbs?</h1>
    <p class="subline">Lights keep flicking off?</p>
    <p class="wallet-line">Burning<br>a hole<br>in your wallet?</p>
  </section>
</div>
</body>
</html>
```